New Business Card Design*

We are a recruitment company based in Norwich/Cambridge England.
I have included our company logo which we want to remain the same.

What we are looking for is a new creative Business card which will really stand out!!

Contact Information for Business Card

Harriet Dunmore
email: Harriet@vexalim.co.uk
Address: Larkwell House
Brambleton Enterprise Quarter
Thistlebrook Road
Norwich
QX9 2LB
Tel:01632 418305

```html
<!DOCTYPE html>
<html lang="en">
<head>
<meta charset="utf-8">
<title>Vexalim Business Card</title>
<link href="https://fonts.googleapis.com/css2?family=Open+Sans:wght@400;600;700&display=swap" rel="stylesheet">
<style>
  :root {
    --stage: #2b2e31;
    --card-dark: #050505;
    --card-light: #ffffff;
    --brand-green: #7ac143;
    --brand-grey: #8b888d;
    --ink: #5a5a5c;
  }
  * { box-sizing: border-box; margin: 0; padding: 0; }
  html, body {
    width: 1200px;
    height: 900px;
    overflow: hidden;
    background: var(--stage);
    font-family: "Open Sans", Arial, sans-serif;
  }
  .stage {
    position: relative;
    width: 1200px;
    height: 900px;
    display: flex;
    align-items: center;
    justify-content: center;
    gap: 40px;
  }
  .card {
    position: relative;
    width: 500px;
    height: 290px;
    border-radius: 22px;
    overflow: hidden;
  }
  .card--front { background: var(--card-dark); }
  .card--back { background: var(--card-light); }

  .brand {
    display: flex;
    align-items: center;
    gap: 14px;
  }
  .brand__dot {
    width: 40px;
    height: 40px;
    border-radius: 50%;
    background: var(--brand-green);
    flex: none;
  }
  .brand__name {
    font-weight: 700;
    color: var(--brand-green);
    line-height: 1;
    letter-spacing: -1px;
  }
  .brand__tagline {
    color: var(--brand-grey);
    font-weight: 600;
    text-transform: none;
  }

  /* Front */
  .card--front .lockup {
    position: absolute;
    left: 50%;
    top: 50%;
    transform: translate(-50%, -50%);
    text-align: center;
  }
  .card--front .brand__dot { width: 52px; height: 52px; }
  .card--front .brand__name { font-size: 72px; }
  .card--front .brand__tagline {
    margin-top: 10px;
    font-size: 13px;
    letter-spacing: 6px;
  }

  /* Back */
  .card--back .lockup {
    position: absolute;
    right: 30px;
    top: 26px;
    text-align: right;
  }
  .card--back .brand__dot { width: 30px; height: 30px; }
  .card--back .brand__name { font-size: 42px; }
  .card--back .brand__tagline {
    margin-top: 6px;
    font-size: 8.5px;
    letter-spacing: 3.4px;
  }
  .contact {
    position: absolute;
    color: var(--ink);
    font-weight: 600;
    letter-spacing: 2px;
  }
  .contact__name {
    left: 32px;
    top: 118px;
    font-size: 19px;
  }
  .contact__email {
    left: 32px;
    top: 148px;
    font-size: 14px;
  }
  .contact__address {
    left: 32px;
    bottom: 28px;
    font-size: 11px;
    line-height: 1.6;
  }
  .contact__city {
    right: 30px;
    bottom: 28px;
    font-size: 11px;
    line-height: 1.6;
    text-align: right;
  }
</style>
</head>
<body>
<main class="stage">
  <section class="card card--front" aria-label="Card front">
    <div class="lockup">
      <div class="brand">
        <span class="brand__dot"></span>
        <span class="brand__name">Vexalim</span>
      </div>
      <p class="brand__tagline">Technology Recruitment</p>
    </div>
  </section>

  <section class="card card--back" aria-label="Card back">
    <div class="lockup">
      <div class="brand">
        <span class="brand__dot"></span>
        <span class="brand__name">Vexalim</span>
      </div>
      <p class="brand__tagline">Technology Recruitment</p>
    </div>

    <p class="contact contact__name">Harriet Dunmore</p>
    <p class="contact contact__email">Harriet@vexalim.co.uk</p>

    <address class="contact contact__address" style="font-style: normal;">
      Larkwell House<br>
      Brambleton Enterprise Quarter<br>
      Thistlebrook Road
    </address>

    <p class="contact contact__city">
      Norwich<br>
      QX9 2LB<br>
      Tel:01632 418305
    </p>
  </section>
</main>
</body>
</html>
```